Flyer "Pinch Analysis"-Energy Optimization procedure for Industry

We need a flyer (1xA4 recto/verso )design for a new part of our business.

In Summary: we want to communicate that we are providing "Pinch Analysis" for the industry. It's an energy optimization procedure. We are a cutting edge engineering consulting group.

All details about project in the attached files

Target Market(s)

Engineering

Industry/Entity Type

Business

Font styles to use
Serif

Requirements
Must have
• Finale document in .ai format ready for printing
• More informations in attached files
Nice to have
• See attached files

```html
<!DOCTYPE html>
<html lang="fr">
<head>
<meta charset="utf-8">
<title>Analyse Pinch – Norva</title>
<link href="https://fonts.googleapis.com/css2?family=Open+Sans:wght@300;400;600;700&display=swap" rel="stylesheet">
<style>
  :root {
    --brand-blue: #1f7ec2;
    --title-blue: #5c9ccb;
    --text-grey: #555a60;
    --dark: #2e3338;
    --paper: #ffffff;
  }
  html, body { margin: 0; padding: 0; overflow: hidden; background: var(--paper); }
  .flyer {
    position: relative; width: 849px; height: 1200px; overflow: hidden;
    background: var(--paper); font-family: "Open Sans", Arial, sans-serif; color: var(--text-grey);
  }
  .hero {
    position: absolute; left: 0; top: 0; width: 849px; height: 470px;
    background: linear-gradient(160deg, #cfd6dc 0%, #8e99a3 35%, #5b6670 60%, #a9b2ba 85%, #dfe4e8 100%);
  }
  .brand {
    position: absolute; top: 42px; right: 0; width: 236px; height: 70px;
    background: var(--brand-blue); display: flex; align-items: center; gap: 12px; padding-left: 22px; box-sizing: border-box;
  }
  .brand-dot { width: 14px; height: 14px; border-radius: 50%; background: var(--paper); }
  .brand-name { color: var(--paper); font-weight: 600; font-size: 30px; letter-spacing: 4px; }
  .content { position: absolute; left: 88px; top: 505px; width: 672px; }
  .title { margin: 0; font-weight: 300; font-size: 56px; line-height: 62px; color: var(--title-blue); }
  .subtitle { margin: 2px 0 0; font-weight: 300; font-size: 27px; line-height: 34px; color: var(--text-grey); }
  .intro { margin: 26px 0 0; font-size: 14.5px; line-height: 21px; color: var(--brand-blue); }
  .lead { margin: 20px 0 0; font-size: 13.5px; line-height: 19px; font-weight: 700; color: var(--dark); }
  .questions { margin: 14px 0 0; padding: 0; list-style: none; font-size: 11.5px; line-height: 17px; }
  .questions li::before { content: "• "; }
  .columns { margin-top: 20px; display: grid; grid-template-columns: 1fr 1fr; gap: 26px; font-size: 11.5px; line-height: 16.5px; }
  .columns p { margin: 0; }
  .columns strong { color: var(--dark); }
  .footer { position: absolute; top: 1035px; left: 330px; display: flex; gap: 120px; font-size: 11.5px; line-height: 16.5px; }
  .footer p { margin: 0; }
</style>
</head>
<body>
<div class="flyer">
  <div class="hero" role="img" aria-label="Photographie d'une installation industrielle avec tuyauteries et échangeurs de chaleur"></div>
  <div class="brand"><span class="brand-dot"></span><span class="brand-name">NORVA</span></div>

  <main class="content">
    <h1 class="title">Analyse Pinch –</h1>
    <p class="subtitle">en route vers la performance opérationnelle<br>et l'efficacité énergétique</p>

    <p class="intro">La performance opérationnelle et l'efficacité énergétique sont les clés de la réussite de l'industrie de demain. Fort d'une longue expérience dans l'analyse, la conception et la mise en service d'installations industrielles (chimie, alimentaire, pharmacie,...), la société Norva utilise l'analyse Pinch dans sa démarche de conception et d'amélioration.</p>

    <p class="lead">L'analyse Pinch est une méthode d'analyse systématique développée et appliquée depuis les années 1980; elle permet de répondre aux questions suivantes:</p>

    <ul class="questions">
      <li>Quels sont les besoins de chaleur et de froid minimaux de mon procédé</li>
      <li>Quel est mon potentiel de réduction de consommation énergétique</li>
      <li>Quel est la solution technique présentant les coûts minimaux entre investissements et économies</li>
    </ul>

    <div class="columns">
      <p>L'amélioration de l'efficacité énergétique est liée directement à l'exploitation des potentiels de récupération du procédé. Des potentiels de diminution de la consommation de 10 à 30% sont usuels. <strong>Nous pouvons également améliorer les performances opérationnelles en analysant vos méthodes de fabrication.</strong> <strong>L'analyse Pinch est aussi bien adaptée pour les PME</strong> que pour les grandes entreprises dont les procédés sont exploités de manière continue ou discontinue (batch). Etant donné les objectifs énergétiques de la confédéra-</p>
      <p>tion, l'<strong>Agence nationale de l'énergie (ANE) soutient les analyses Pinch à hauteur de 30% pour les procédés continus et de 60% pour les procédés discontinus (batch).</strong><br>Pour tous compléments d'informations et pour savoir si une analyse Pinch est justifiées dans votre cas, nous vous conseillons avec plaisir.</p>
    </div>
  </main>

  <footer class="footer">
    <p>Norva SA<br>Rue des Acacias 14<br>CH-1900 Valbourg</p>
    <p>Contact:<br>Julien Mercier,<br>Thomas Reynard</p>
  </footer>
</div>
</body>
</html>
```